Brackwell Ponds Trifold About Us Leaflet

I need a A4 Trifold Leaflet Double sided designed with the following information on it:
Logo
Awards
Pictures - Please find on our website www.brackwellponds-example.co.uk or www.facebook.com/brackwellponds
Contact Information
Welcome Text
Events
Ideal for Text
Fishing Text
Camping Text
Map

Target Market(s)

This is almost a paper version of our website.

```html
<!DOCTYPE html>
<html lang="en">
<head>
<meta charset="utf-8">
<title>Brackwell Ponds – Trifold Leaflet</title>
<link href="https://fonts.googleapis.com/css2?family=Roboto+Condensed:wght@400;700&family=Arimo:wght@400;700&family=PT+Sans:wght@400&display=swap" rel="stylesheet">
<style>
  :root{
    --green:#3a9a12;
    --green-dark:#1f6e06;
    --green-light:#6cc12a;
    --ink:#3b3b3b;
    --grey:#555;
    --paper:#ffffff;
    --canvas:#e8e8e6;
  }
  *{margin:0;padding:0;box-sizing:border-box}
  html,body{width:1200px;height:900px;overflow:hidden;background:var(--canvas)}
  .leaflet{position:absolute;left:90px;top:85px;width:1020px;height:727px;background:var(--paper);overflow:hidden;box-shadow:0 4px 18px rgba(0,0,0,.25)}
  .layer{position:absolute;left:0;top:0;width:1020px;height:727px}
  .photo-card{position:absolute;border:5px solid #fff;box-shadow:0 3px 8px rgba(0,0,0,.35)}
  .photo-angler{left:8px;top:26px;width:228px;height:178px;transform:rotate(-10deg);background:linear-gradient(160deg,#5e7a3a,#3f5a2a 55%,#7f8d4c)}
  .photo-bird{left:200px;top:10px;width:212px;height:158px;transform:rotate(7deg);background:linear-gradient(140deg,#7f9a4c,#5b7a33 60%,#a7a58a)}
  .ideal{position:absolute;left:32px;top:234px;width:250px;color:#fff;font-family:"Arimo",sans-serif}
  .ideal h2{font-size:17px;font-weight:700;margin-bottom:10px;white-space:nowrap}
  .ideal ul{list-style:none;width:220px}
  .ideal li{position:relative;padding-left:22px;font-size:12px;line-height:14px;margin-bottom:12px}
  .ideal li::before{content:"";position:absolute;left:0;top:3px;width:9px;height:9px;background:#fff}
  .ideal b{color:#0d2a02;font-family:"Roboto Condensed",sans-serif}
  .ideal b.hl{color:#fff}
  .welcome-story{position:absolute;left:40px;top:500px;width:292px;font-family:"PT Sans",sans-serif;color:var(--ink);font-size:11.6px;line-height:14.6px;text-align:justify}
  .welcome-story h2{font-family:"Arimo",sans-serif;color:var(--green-dark);font-size:16px;font-weight:700;margin-bottom:3px;padding-left:3px}
  .welcome-story p{margin-bottom:8px}
  .welcome-story p.tight{margin-bottom:0}
  .contact{position:absolute;left:406px;top:155px;font-family:"Roboto Condensed",sans-serif;color:var(--ink)}
  .contact h3{color:var(--green-dark);font-size:17px;font-weight:700;letter-spacing:.5px;margin-bottom:6px}
  .contact .line{display:flex;align-items:center;gap:10px;font-weight:700;font-size:17px;height:22px;margin-left:26px}
  .contact .web{margin-left:12px;font-size:14.5px;height:20px}
  .contact .gap{height:8px}
  .contact svg{flex:none}
  .logo-box{position:absolute;left:768px;top:52px;width:164px;height:70px;background:#fff;border:1px solid #aaa;display:flex;align-items:center;justify-content:center;gap:6px}
  .logo-box .mark{width:9px;height:9px;background:var(--green)}
  .logo-box span{font-family:"Arimo",sans-serif;color:var(--green-dark);font-size:16px;font-weight:700}
  .tagline{position:absolute;left:680px;top:558px;width:340px;text-align:center;font-family:"Roboto Condensed",sans-serif;font-weight:700}
  .tagline h2{color:var(--green-dark);font-size:30px;letter-spacing:1px;margin-bottom:8px}
  .tagline p{color:var(--grey);font-size:14px;line-height:18px;letter-spacing:.4px}
  .tagline .pace{color:var(--green);margin-top:4px}
</style>
</head>
<body>
<main class="leaflet">
  <svg class="layer" viewBox="0 0 1020 727" aria-hidden="true">
    <defs>
      <linearGradient id="mid-paper" x1="0" x2="1">
        <stop offset="0" stop-color="#d9d9d9"/><stop offset=".45" stop-color="#ffffff"/><stop offset="1" stop-color="#d2d2d2"/>
      </linearGradient>
      <linearGradient id="green-fill" x1="0" y1="0" x2="0" y2="1">
        <stop offset="0" stop-color="var(--green-light)"/><stop offset="1" stop-color="var(--green-dark)"/>
      </linearGradient>
    </defs>
    <rect x="338" y="0" width="342" height="727" fill="url(#mid-paper)"/>
    <path d="M0,0H338V392Q170,420 0,515Z" fill="url(#green-fill)"/>
    <path d="M0,515Q170,420 338,392V404Q170,432 0,530Z" fill="#2d2d2d" opacity=".75"/>
    <path d="M680,0H1020V118H680Z" fill="url(#green-fill)"/>
    <path d="M470,398C600,398 660,520 780,515C880,510 960,440 1020,380V430C960,490 880,545 780,545C660,545 600,430 470,412Z" fill="url(#green-fill)"/>
    <path d="M470,412C600,430 660,545 780,545C880,545 960,490 1020,430V442C960,502 880,557 780,557C660,557 600,442 470,424Z" fill="#2d2d2d" opacity=".7"/>
  </svg>

  <div class="photo-card photo-angler" role="img" aria-label="Photo: angler holding a carp by the lake"></div>
  <div class="photo-card photo-bird" role="img" aria-label="Photo: kingfisher perched on a rail"></div>

  <svg class="layer" viewBox="0 0 1020 727" role="img" aria-label="Photo: farmhouse with lawn and fence">
    <defs><linearGradient id="house" x1="0" y1="0" x2="0" y2="1"><stop offset="0" stop-color="#dfe3e4"/><stop offset=".45" stop-color="#7a8a5c"/><stop offset="1" stop-color="#5f8a2e"/></linearGradient></defs>
    <path d="M680,118H1020V380C960,440 880,510 780,515C740,517 705,505 680,490Z" fill="url(#house)"/>
  </svg>

  <svg class="layer" viewBox="0 0 1020 727" role="img" aria-label="Photo: willow trees and bridge over the pond">
    <defs><linearGradient id="pond" x1="0" y1="0" x2="0" y2="1"><stop offset="0" stop-color="#c8d3cf"/><stop offset=".4" stop-color="#4d6b34"/><stop offset="1" stop-color="#2c4520"/></linearGradient></defs>
    <path d="M338,440C400,428 440,422 470,424C600,442 650,540 680,552V727H338Z" fill="url(#pond)"/>
  </svg>

  <svg class="layer" viewBox="0 0 1020 727" role="img" aria-label="Photo: rainbow over a tree in the camping field">
    <defs><linearGradient id="rain" x1="0" y1="0" x2="0" y2="1"><stop offset="0" stop-color="#8d9290"/><stop offset=".55" stop-color="#a99a4a"/><stop offset="1" stop-color="#6e8a3a"/></linearGradient></defs>
    <circle cx="372" cy="388" r="102" fill="#fff"/>
    <circle cx="372" cy="388" r="95" fill="url(#rain)"/>
  </svg>

  <section class="ideal">
    <h2>Brackwell Ponds is ideal for;</h2>
    <ul>
      <li><b>Walking</b> – The Millbrook Trail is 220mtrs from the campsite</li>
      <li><b>Cycling</b> – Somerset is cris crossed with cycle paths</li>
      <li><b>Bird watching</b> – Over 70 species on site(WBT survey) and there are lots of <b class="hl">WBT sites locally</b></li>
    </ul>
  </section>

  <section class="welcome-story">
    <h2>Welcome</h2>
    <p>The Ashdown family established Brackwell Ponds in 1993 from their traditional family farm, over the years it has become home to nightingales, kingfishers, deer and foxes to name but a few.</p>
    <p>Just a short level walk from the campsite there are about 2 miles of off road walking ideal for spotting some of the wildlife or may be just chatting to the fisher folk about the one that got away.</p>
    <p class="tight">There is a abundance of local attractions to visit and plenty to see.</p>
    <p>Whether it is just 1 night or 14 nights Brackwell Ponds welcomes you all.</p>
  </section>

  <section class="contact">
    <h3>YOU CAN NOW BOOK ONLINE</h3>
    <div class="line"><svg width="13" height="13" viewBox="0 0 13 13"><rect width="13" height="13" rx="2" fill="var(--green)"/><path d="M3.5,3 L5.2,3 6,5 5,6 Q6,8 7.2,8.6 L8,7.6 10,8.4 10,10 Q6,10.5 3.5,3Z" fill="#fff"/></svg>01632 960418</div>
    <div class="line"><svg width="13" height="13" viewBox="0 0 13 13"><rect width="13" height="13" rx="2" fill="var(--green)"/><path d="M3.5,3 L5.2,3 6,5 5,6 Q6,8 7.2,8.6 L8,7.6 10,8.4 10,10 Q6,10.5 3.5,3Z" fill="#fff"/></svg>07700900316</div>
    <div class="gap"></div>
    <div class="line web"><svg width="16" height="16" viewBox="0 0 16 16"><circle cx="8" cy="8" r="7" fill="none" stroke="var(--green)" stroke-width="1.6"/><path d="M1,8H15M8,1V15M3,4H13M3,12H13" stroke="var(--green)" stroke-width="1.2"/></svg>www.brackwellponds-example.co.uk</div>
    <div class="line web"><svg width="16" height="12" viewBox="0 0 16 12"><rect width="16" height="12" fill="var(--green)"/><path d="M1,1L8,7 15,1" fill="none" stroke="#fff" stroke-width="1.4"/></svg>info@brackwellponds-example.co.uk</div>
  </section>

  <div class="logo-box"><i class="mark"></i><span>Brackwell Ponds</span></div>

  <section class="tagline">
    <h2>WELCOME</h2>
    <p>A HAVEN OF PEACE, QUIET AND RELAXATION<br>SO RELAX, SOAK UP THE SILENCE LIVE LIFE</p>
    <p class="pace">AT THE GENTLER PACE</p>
  </section>
</main>
</body>
</html>
```